Business card (AI file uploaded)

We need a business card design that is minimalist using existing logo (attached). Source files must be editable so we can make the same design with other names.

Screenshots included of a design I was working on to give you an idea of the style I would like. Looking for similar modern styles

Thanks

```html
<!DOCTYPE html>
<html lang="en">
<head>
<meta charset="UTF-8">
<title>Verdane Law Group – Business Card</title>
<link href="https://fonts.googleapis.com/css2?family=Source+Sans+3:wght@400;600&display=swap" rel="stylesheet">
<style>
  :root {
    --stage: #2b2b2b;
    --card-center: #3a3a3a;
    --card-edge: #0c0c0c;
    --teal: #17a9a3;
    --white: #ffffff;
    --text-soft: #e9e9e9;
  }
  * { margin: 0; padding: 0; box-sizing: border-box; }
  html, body {
    width: 1200px; height: 1000px; overflow: hidden;
    background: var(--stage);
    font-family: "Source Sans 3", sans-serif;
    color: var(--white);
  }
  .stage { position: relative; width: 1200px; height: 1000px; }

  .card {
    position: absolute;
    overflow: hidden;
    box-shadow: 0 20px 50px rgba(0,0,0,.6);
  }
  .card-surface {
    position: absolute; inset: 0;
    background: radial-gradient(ellipse at 50% 45%, var(--card-center) 0%, #1c1c1c 55%, var(--card-edge) 100%);
  }

  /* Front card */
  .card-front { left: 80px; top: 140px; width: 420px; height: 720px; }
  .front-mark {
    position: absolute; left: 50%; top: 200px; transform: translateX(-50%);
    width: 118px; height: 118px; border-radius: 50%;
    border: 7px solid var(--white);
  }
  .front-wordmark {
    position: absolute; left: 0; right: 0; top: 400px;
    text-align: center; font-weight: 400; color: var(--white);
    line-height: 1;
  }
  .wordmark-primary { display: block; font-size: 74px; letter-spacing: 2px; }
  .wordmark-secondary { display: block; font-size: 40px; letter-spacing: 9px; margin-top: 6px; }
  .practice-band {
    position: absolute; left: 0; right: 0; bottom: 40px; height: 38px;
    background: var(--teal);
    display: flex; align-items: center; justify-content: center;
    font-size: 19px; color: var(--white);
  }
  .practice-band .divider { margin: 0 6px; }

  /* Back card */
  .card-back { left: 540px; top: 270px; width: 620px; height: 420px; }
  .accent-bar {
    position: absolute; left: 40px; width: 26px; background: var(--teal);
  }
  .accent-top { top: -20px; height: 150px; border-radius: 0 0 13px 13px; }
  .accent-bottom { top: 300px; height: 140px; border-radius: 13px 13px 0 0; }
  .person-name {
    position: absolute; left: 90px; top: 70px;
    font-size: 44px; font-weight: 600; color: var(--teal);
  }
  .person-title {
    position: absolute; left: 92px; top: 126px;
    font-size: 20px; color: var(--text-soft);
  }
  .back-mark {
    position: absolute; right: 40px; top: 130px;
    width: 74px; height: 74px; border-radius: 50%;
    border: 5px solid var(--white);
  }
  .contact-list { position: absolute; left: 40px; top: 175px; list-style: none; }
  .contact-item {
    display: flex; align-items: center; gap: 16px;
    font-size: 20px; color: var(--white); margin-bottom: 16px;
  }
  .contact-icon { width: 28px; height: 28px; flex: none; }
  .contact-item .gap { margin-left: 22px; }
</style>
</head>
<body>
<main class="stage">

  <section class="card card-front">
    <div class="card-surface" role="img" aria-label="Dark card surface with a subtle dotted pattern"></div>
    <div class="front-mark"></div>
    <div class="front-wordmark">
      <span class="wordmark-primary">VERDANE</span>
      <span class="wordmark-secondary">LAW GROUP PC</span>
    </div>
    <div class="practice-band">
      Real Estate<span class="divider">|</span>Bankruptcy<span class="divider">|</span>Social Security Disability
    </div>
  </section>

  <section class="card card-back">
    <div class="card-surface" role="img" aria-label="Dark card surface with a subtle dotted pattern"></div>
    <div class="accent-bar accent-top"></div>
    <div class="accent-bar accent-bottom"></div>
    <h1 class="person-name">Marcus Verdane</h1>
    <p class="person-title">Attorney At Law</p>
    <div class="back-mark"></div>
    <ul class="contact-list">
      <li class="contact-item">
        <svg class="contact-icon" viewBox="0 0 28 28"><circle cx="14" cy="14" r="14" fill="#17a9a3"/><path d="M14 6a5.5 5.5 0 0 0-5.5 5.5C8.5 16 14 22 14 22s5.5-6 5.5-10.5A5.5 5.5 0 0 0 14 6z" fill="#111"/><circle cx="14" cy="11.5" r="2" fill="#17a9a3"/></svg>
        418 Harbor Ave., Suite 210, Lakeview, IL 60614
      </li>
      <li class="contact-item">
        <svg class="contact-icon" viewBox="0 0 28 28"><circle cx="14" cy="14" r="14" fill="#17a9a3"/><rect x="7" y="12" width="14" height="8" rx="1.5" fill="#111"/><rect x="10" y="7" width="8" height="6" fill="#111"/><rect x="9" y="9" width="3" height="9" rx="1.5" fill="#17a9a3"/></svg>
        P: 630.555.0142<span class="gap">F: 630.555.0187</span>
      </li>
      <li class="contact-item">
        <svg class="contact-icon" viewBox="0 0 28 28"><circle cx="14" cy="14" r="14" fill="#17a9a3"/><rect x="7" y="9" width="14" height="10" fill="#111"/><path d="M7 9l7 6 7-6" fill="none" stroke="#17a9a3" stroke-width="1.5"/></svg>
        mverdane@verdanelaw.com
      </li>
    </ul>
  </section>

</main>
</body>
</html>
```